WordPress Website for Accounting Firm

I have attached an excel sheet showing what i need done for my accounting website. Currently i have a WP website but its not live and do not like it. I can give a link if that will help. Total pages is around 12. I can buy and supply the images but have provided indication of what i want in the excel. I will need the designer to do the coding to make the website fully functional. I want a clean look and attractive. Don't want too dark colors. Once i like the landing page, i will need the designer to code code the website. Just want to look first. I will provide the logo file and put the contents myself. Just put dummy contents for now to show how it will look.
Updates
Can you please use the attached images so i can see how nit will look on the coverage as an option. These are from pixelharbor
264918053
418273596
1537206419
1096382147
Currently there are only 2 provided by myself as Photo 1 and Photo 2
Many Thanks!
Industry/Entity Type
Accounting and Finance
Number of Pages Required
5+ page

```html
<!DOCTYPE html>
<html lang="en">
<head>
<meta charset="utf-8">
<title>Ledgerline Advisory — Accounting &amp; Tax</title>
<link href="https://fonts.googleapis.com/css2?family=Roboto:wght@300;400;500;700;900&family=Lora:ital@1&display=swap" rel="stylesheet">
<style>
:root{
  --green:#5b9f4f;
  --green-band:#62a257;
  --green-dark:#2f8a24;
  --ink:#111111;
  --body:#444444;
  --muted:#555555;
  --light-bg:#f6f6f6;
  --footer:#2b2b2b;
  --white:#ffffff;
}
*{box-sizing:border-box;margin:0;padding:0}
html,body{width:1200px;height:3484px;overflow:hidden}
body{position:relative;font-family:"Roboto",sans-serif;color:var(--ink);background:var(--white)}

/* header */
.site-header{position:absolute;left:0;top:0;width:1200px;height:87px;background:var(--white)}
.brand{position:absolute;left:111px;top:6px;height:75px;display:flex;align-items:center;gap:12px}
.brand-mark{width:66px;height:66px;border:6px solid #6f6f6f;border-radius:50%}
.brand-name{font-size:17px;font-weight:400;color:#6f6f6f;letter-spacing:.5px}
.main-nav{position:absolute;top:35px;left:0;width:1200px;font-size:15px;font-weight:400;color:#333}
.main-nav a{position:absolute;white-space:nowrap;color:inherit;text-decoration:none}

/* hero */
.hero{position:absolute;left:0;top:87px;width:1200px;height:644px;overflow:hidden;
  background:
   radial-gradient(ellipse 520px 300px at 560px 300px, rgba(170,195,215,.95), rgba(170,195,215,0) 70%),
   radial-gradient(ellipse 400px 160px at 500px 120px, rgba(230,200,150,.8), rgba(230,200,150,0) 70%),
   linear-gradient(180deg,#5b3a22 0%,#8a5a33 35%,#6a4a30 70%,#3a2a1c 100%)}
.hero-title{position:absolute;left:114px;top:190px;font-size:57px;line-height:52px;font-weight:700;color:var(--white);text-transform:uppercase}
.hero-text{position:absolute;left:114px;top:313px;width:480px;font-size:19px;line-height:36px;font-weight:700;color:var(--white)}
.btn{position:absolute;display:flex;align-items:center;justify-content:center;background:var(--green);color:var(--white);
  font-weight:500;border-radius:30px;text-decoration:none;text-transform:uppercase}
.hero .btn{left:112px;top:407px;width:173px;height:46px;font-size:16px}
.hero-arrow{position:absolute;top:313px;width:30px;height:52px}
.dots{position:absolute;top:606px;left:0;width:1200px}
.dots span{position:absolute;width:13px;height:13px;border-radius:50%;background:rgba(255,255,255,.55)}
.dots span.active{background:var(--white)}

/* about */
.about-title{position:absolute;left:0;top:803px;width:1200px;text-align:center;font-size:39px;font-weight:700}
.about-text{position:absolute;left:100px;top:864px;width:1000px;text-align:center;font-size:15px;line-height:29px;color:var(--body);white-space:nowrap}
.about .btn{left:514px;top:1034px;width:172px;height:46px;font-size:16px}

/* why */
.why{position:absolute;left:0;top:1169px;width:1200px;height:590px;background:var(--light-bg)}
.why-art{position:absolute;left:0;top:0;width:630px;height:590px}
.why-title{position:absolute;left:634px;top:48px;font-size:40px;font-weight:700}
.why-list{position:absolute;left:634px;top:110px;width:460px;list-style:none;font-size:15.5px;line-height:24.5px;color:#333}
.why-list li{position:absolute;left:0;padding-left:27px;width:460px}
.why-list svg{position:absolute;left:0;top:3px}

/* testimonials */
.testimonials{position:absolute;left:0;top:1759px;width:1200px;height:557px;background:var(--green-band)}
.testimonials h2{position:absolute;left:0;top:73px;width:1225px;text-align:center;font-size:39px;font-weight:700;color:var(--white)}
.quote-card{position:absolute;top:143px;width:471px;height:330px;background:var(--white);border-radius:6px;box-shadow:0 3px 10px rgba(0,0,0,.18)}
.quote-card svg.q{position:absolute;left:22px;top:24px}
.quote-text{position:absolute;left:22px;top:78px;width:440px;font-family:"Lora",serif;font-style:italic;font-size:17.5px;line-height:34.3px;color:var(--muted);white-space:nowrap}
.avatar{position:absolute;left:22px;top:258px;width:56px;height:56px;border-radius:50%;background:#b9b2aa}
.q-name{position:absolute;left:91px;top:265px;font-size:18.5px;font-weight:500;color:var(--ink)}
.q-date{position:absolute;left:91px;top:294px;font-size:14px;color:#333;letter-spacing:.5px}
.t-arrow{position:absolute;top:283px;width:28px;height:52px}

/* industries */
.ind-title{position:absolute;left:0;top:2390px;width:1200px;text-align:center;font-size:40px;font-weight:700}
.tile{position:absolute;width:235px}
.tile .photo{width:235px;height:222px}
.tile figcaption{margin-top:8px;text-align:center;font-size:17.5px;font-weight:500;color:var(--ink)}
.industries .btn{left:529px;top:3020px;width:141px;height:41px;font-size:14px}

/* footer */
.site-footer{position:absolute;left:0;top:3143px;width:1200px;height:341px;background:var(--footer);color:var(--white)}
.f-brand{position:absolute;left:111px;top:68px;display:flex;align-items:center;gap:14px}
.f-brand .brand-mark{width:88px;height:88px;border:6px solid var(--white)}
.f-brand .brand-name{color:var(--white);font-size:19px}
.f-social{position:absolute;left:221px;top:169px;width:32px;height:32px;border-radius:50%;background:#555}
.f-col{position:absolute;top:70px}
.f-col h3{font-size:18.5px;font-weight:700;text-transform:uppercase;margin-bottom:11px;white-space:nowrap}
.f-col li{list-style:none;font-size:13.5px;line-height:25.7px;white-space:nowrap}
.f-rule{position:absolute;left:115px;top:275px;width:976px;height:1px;background:#777}
.copyright{position:absolute;left:0;top:296px;width:1200px;text-align:center;font-size:13.5px}
</style>
</head>
<body>

<header class="site-header">
  <div class="brand"><span class="brand-mark"></span><span class="brand-name">LEDGERLINE ADVISORY</span></div>
  <nav class="main-nav">
    <a style="left:521px">HOME</a>
    <a style="left:602px">SOLUTIONS</a>
    <a style="left:722px">CLIENTS</a>
    <a style="left:820px">CLIENT RESOURSES</a>
    <a style="left:997px">CONTACT US</a>
  </nav>
</header>

<section class="hero" role="img" aria-label="Photo of a rock climber hanging from a sea cave ceiling above a coastal bay at sunset">
  <h1 class="hero-title">Ledgerline<br>Advisory</h1>
  <p class="hero-text">Lorem ipsum dolor sit amet, consectetur adipiscing<br>elit, sed do eiusmod tempor incididunt</p>
  <a class="btn">Get Started</a>
  <svg class="hero-arrow" style="left:69px" viewBox="0 0 30 52"><path d="M28 2 L3 26 L28 50" fill="none" stroke="#fff" stroke-width="2"/></svg>
  <svg class="hero-arrow" style="left:1096px" viewBox="0 0 30 52"><path d="M2 2 L27 26 L2 50" fill="none" stroke="#fff" stroke-width="2"/></svg>
  <div class="dots"><span style="left:554px"></span><span class="active" style="left:580px"></span><span style="left:606px"></span><span style="left:633px"></span></div>
</section>

<section class="about">
  <h2 class="about-title">ABOUT US</h2>
  <p class="about-text">Lorem ipsum dolor sit amet, consectetur adipiscing elit, sed do eiusmod tempor incididunt ut labore et dolore magna aliqua. Quis ipsum<br>suspendisse ultrices gravida. Risus commodo viverra maecenas accumsan lacus vel facilisis. Lorem ipsum dolor sit amet, consectetur<br>adipiscing elit, sed do eiusmod tempor incididunt ut labore et dolore magna aliqua. Quis ipsum suspendisse ultrices gravida. Risus<br>commodo viverra maecenas accumsan lacus vel facilisis. Lorem ipsum dolor sit amet, consectetur adipiscing elit, sed do eiusmod<br>tempor incididunt ut labore et dolore magna aliqua. Quis ipsum suspendisse ultrices gravida.</p>
  <a class="btn">Learn More</a>
</section>

<section class="why">
  <div class="why-art" role="img" aria-label="Abstract illustration of scattered green geometric triangles" style="background:linear-gradient(100deg,#1f8f1a 0%,#16a514 22%,rgba(40,170,30,.55) 45%,rgba(246,246,246,0) 85%)"></div>
  <h2 class="why-title">WHY CHOOSE US</h2>
  <ul class="why-list">
    <li style="top:0"><svg width="20" height="20" viewBox="0 0 20 20"><circle cx="10" cy="10" r="9" fill="none" stroke="#4f9f45" stroke-width="1.5"/><path d="M5.5 10.5 L8.8 13.5 L14.5 7" fill="none" stroke="#4f9f45" stroke-width="1.8"/></svg>We specialise in accounting and tax solutions for all business<br>structures and industries</li>
    <li style="top:57px"><svg width="20" height="20" viewBox="0 0 20 20"><circle cx="10" cy="10" r="9" fill="none" stroke="#4f9f45" stroke-width="1.5"/><path d="M5.5 10.5 L8.8 13.5 L14.5 7" fill="none" stroke="#4f9f45" stroke-width="1.8"/></svg>Our team are qualified professionals with 50+ years of<br>combined experience in CA industry</li>
    <li style="top:118px"><svg width="20" height="20" viewBox="0 0 20 20"><circle cx="10" cy="10" r="9" fill="none" stroke="#4f9f45" stroke-width="1.5"/><path d="M5.5 10.5 L8.8 13.5 L14.5 7" fill="none" stroke="#4f9f45" stroke-width="1.8"/></svg>We are Accessable 7 days a week</li>
    <li style="top:158px"><svg width="20" height="20" viewBox="0 0 20 20"><circle cx="10" cy="10" r="9" fill="none" stroke="#4f9f45" stroke-width="1.5"/><path d="M5.5 10.5 L8.8 13.5 L14.5 7" fill="none" stroke="#4f9f45" stroke-width="1.8"/></svg>We constantly upskill to keep up with changes to tax laws<br>and legislation</li>
    <li style="top:220px"><svg width="20" height="20" viewBox="0 0 20 20"><circle cx="10" cy="10" r="9" fill="none" stroke="#4f9f45" stroke-width="1.5"/><path d="M5.5 10.5 L8.8 13.5 L14.5 7" fill="none" stroke="#4f9f45" stroke-width="1.8"/></svg>Our advise is explained in plain english so you understand</li>
    <li style="top:260px"><svg width="20" height="20" viewBox="0 0 20 20"><circle cx="10" cy="10" r="9" fill="none" stroke="#4f9f45" stroke-width="1.5"/><path d="M5.5 10.5 L8.8 13.5 L14.5 7" fill="none" stroke="#4f9f45" stroke-width="1.8"/></svg>Our fees are not only fair but very competitive</li>
    <li style="top:300px"><svg width="20" height="20" viewBox="0 0 20 20"><circle cx="10" cy="10" r="9" fill="none" stroke="#4f9f45" stroke-width="1.5"/><path d="M5.5 10.5 L8.8 13.5 L14.5 7" fill="none" stroke="#4f9f45" stroke-width="1.8"/></svg>We don’t believe in one size fits all, we listen to client’s<br>challenges indiviually</li>
    <li style="top:361px"><svg width="20" height="20" viewBox="0 0 20 20"><circle cx="10" cy="10" r="9" fill="none" stroke="#4f9f45" stroke-width="1.5"/><path d="M5.5 10.5 L8.8 13.5 L14.5 7" fill="none" stroke="#4f9f45" stroke-width="1.8"/></svg>We have affiliations with other business partners</li>
    <li style="top:401px"><svg width="20" height="20" viewBox="0 0 20 20"><circle cx="10" cy="10" r="9" fill="none" stroke="#4f9f45" stroke-width="1.5"/><path d="M5.5 10.5 L8.8 13.5 L14.5 7" fill="none" stroke="#4f9f45" stroke-width="1.8"/></svg>We keep up with everchanging cloud based technology</li>
  </ul>
</section>

<section class="testimonials">
  <h2>WHAT CLIENTS SAY</h2>
  <svg class="t-arrow" style="left:60px" viewBox="0 0 28 52"><path d="M26 2 L3 26 L26 50" fill="none" stroke="#fff" stroke-width="2"/></svg>
  <svg class="t-arrow" style="left:1111px" viewBox="0 0 28 52"><path d="M2 2 L25 26 L2 50" fill="none" stroke="#fff" stroke-width="2"/></svg>
  <article class="quote-card" style="left:112px">
    <svg class="q" width="46" height="38" viewBox="0 0 46 38"><path d="M2 36 V20 C2 8 8 2 18 1 V8 C12 9 10 13 10 18 H20 V36 Z M26 36 V20 C26 8 32 2 42 1 V8 C36 9 34 13 34 18 H44 V36 Z" fill="#4f9f45"/></svg>
    <p class="quote-text">Lorem ipsum dolor sit amet, consectetur adipiscing<br>elit, sed do eiusmod tempor incididunt ut labore et<br>dolore magna aliqua. Quis ipsumspendisse ultrices<br>gravida. Risus commodverra maecenas accumsan<br>lacus vel facilisis.</p>
    <div class="avatar" role="img" aria-label="Client portrait photo"></div>
    <p class="q-name">John Smith</p>
    <p class="q-date">08-04-2022</p>
  </article>
  <article class="quote-card" style="left:618px">
    <svg class="q" width="46" height="38" viewBox="0 0 46 38"><path d="M2 36 V20 C2 8 8 2 18 1 V8 C12 9 10 13 10 18 H20 V36 Z M26 36 V20 C26 8 32 2 42 1 V8 C36 9 34 13 34 18 H44 V36 Z" fill="#4f9f45"/></svg>
    <p class="quote-text">Lorem ipsum dolor sit amet, consectetur adipiscing<br>elit, sed do eiusmod tempor incididunt ut labore et<br>dolore magna aliqua. Quis ipsumspendisse ultrices<br>gravida. Risus commodverra maecenas accumsan<br>lacus vel facilisis.</p>
    <div class="avatar" role="img" aria-label="Client portrait photo"></div>
    <p class="q-name">John Smith</p>
    <p class="q-date">08-04-2022</p>
  </article>
</section>

<section class="industries">
  <h2 class="ind-title">INDUSTRIES WE REPRESENT</h2>
  <figure class="tile" style="left:111px;top:2468px"><div class="photo" role="img" aria-label="Photo of a nurse in scrubs using a tablet" style="background:linear-gradient(160deg,#e4e4e2,#7fa9ad 60%,#2f6f7a)"></div><figcaption>Healthcare Specialists</figcaption></figure>
  <figure class="tile" style="left:359px;top:2468px"><div class="photo" role="img" aria-label="Photo of a contractor working on a roof frame" style="background:linear-gradient(160deg,#4a4d52,#c9a57a 55%,#8b6a45)"></div><figcaption>Contractors</figcaption></figure>
  <figure class="tile" style="left:606px;top:2468px"><div class="photo" role="img" aria-label="Photo of a robotic manufacturing line" style="background:linear-gradient(180deg,#cfd3d6,#8e959b 50%,#b89a4a)"></div><figcaption>Manufacturing</figcaption></figure>
  <figure class="tile" style="left:854px;top:2468px"><div class="photo" role="img" aria-label="Photo of cranes over a building construction site" style="background:linear-gradient(180deg,#3f8fd8,#9cc8ec 55%,#b7b0a2)"></div><figcaption>Construction</figcaption></figure>
  <figure class="tile" style="left:111px;top:2734px"><div class="photo" role="img" aria-label="Photo looking up at glass skyscrapers with sunlight" style="background:linear-gradient(135deg,#f4c46a,#d9e4ee 35%,#3b5d7c)"></div><figcaption>Architecture</figcaption></figure>
  <figure class="tile" style="left:359px;top:2734px"><div class="photo" role="img" aria-label="Photo of a house with a for rent sign on the lawn" style="background:linear-gradient(180deg,#d9dcd8,#8f7f72 50%,#5d8a3a)"></div><figcaption>Real Estate Rentals</figcaption></figure>
  <figure class="tile" style="left:606px;top:2734px"><div class="photo" role="img" aria-label="Photo of a service worker holding a clipboard" style="background:linear-gradient(180deg,#efe3c6,#c9b48a 45%,#2d4a78)"></div><figcaption>Professional Services</figcaption></figure>
  <figure class="tile" style="left:854px;top:2734px"><div class="photo" role="img" aria-label="Photo of a clothing retail store interior" style="background:linear-gradient(180deg,#e9e7e3,#9aa3ad 55%,#6b4a3a)"></div><figcaption>Retail</figcaption></figure>
  <a class="btn">View All</a>
</section>

<footer class="site-footer">
  <div class="f-brand"><span class="brand-mark"></span><span class="brand-name">LEDGERLINE ADVISORY</span></div>
  <span class="f-social"></span>
  <div class="f-col" style="left:433px"><h3>Quick Links</h3><ul><li>Home</li><li>Solutions</li><li>Clients</li><li>Contact Us</li><li>Client Resourses</li></ul></div>
  <div class="f-col" style="left:616px"><h3>Customer Service</h3><ul><li>Privacy Policy</li><li>Terms of Conditions</li><li>Sitemap</li><li>FAQ's</li></ul></div>
  <div class="f-col" style="left:856px"><h3>Contact Info</h3><ul><li>P O Box 52907, Harbourside, Auckland 2150</li><li>021 587 416</li><li>info@ledgerline.co.nz</li><li>mara@ledgerline.co.nz</li></ul></div>
  <div class="f-rule"></div>
  <p class="copyright">Copyright © 2022 LEDGERLINE All Rights Reserved.</p>
</footer>

</body>
</html>
```